Verostel business card

Business card for sustainable investment company called "Verostel". Verostel is an exchange platform selling carbon credits between buyers and sellers. Carbon Credits are an environmental commodity for reducing global carbon emissions.

the card should obviously have our logo and the theme should be sustainability/environment mixed with a trading platform.

Contact Information for Business Card

Logo, Name, Title, Phone, Email

Colors
0054AA
0677BA
7BADD7
CADEEF
E8F1F8
0094D4
00A9DD
6FCCEA
C7EBF8
E9F6FB
00AB8E
00BBA5
67D7C9
C6EFE9
E9F9F6
59FF00
82FF00
B8FF75
E3FFCB
F4FFEA

```html
<!DOCTYPE html>
<html lang="en">
<head>
<meta charset="utf-8">
<title>Verostel business card</title>
<link rel="stylesheet" href="https://fonts.googleapis.com/css2?family=Montserrat:wght@600&family=Raleway:wght@400;600&display=swap">
<style>
  :root {
    --backdrop: #b3b3b3;
    --paper: #ffffff;
    --deep-blue: #1a6ee8;
    --aqua: #33e8ee;
    --ink: #1f3250;
    --text: #333333;
  }
  * { margin: 0; padding: 0; box-sizing: border-box; }
  html, body { width: 1000px; height: 1200px; overflow: hidden; }
  body { background: var(--backdrop); position: relative; font-family: "Raleway", sans-serif; }
  .card { position: absolute; left: 50px; width: 899px; height: 540px; background: var(--paper); overflow: hidden; }
  .card--front { top: 43px; }
  .card--back { top: 617px; }
  .card-waves { position: absolute; inset: 0; width: 100%; height: 100%; }
  .brand { position: absolute; display: flex; align-items: center; }
  .brand-mark { display: block; border-radius: 6px; }
  .brand-name { font-family: "Montserrat", sans-serif; font-weight: 600; letter-spacing: 0.5px; line-height: 1; }
  .card--front .brand { left: 113px; top: 245px; gap: 34px; }
  .card--front .brand-mark { width: 48px; height: 48px; background: linear-gradient(90deg, var(--aqua), var(--deep-blue)); }
  .card--front .brand-name { font-size: 52px; color: var(--ink); }
  .card--back .brand { left: 218px; top: 260px; gap: 40px; }
  .card--back .brand-mark { width: 56px; height: 56px; background: var(--paper); }
  .card--back .brand-name { font-size: 62px; color: var(--paper); }
  .person { position: absolute; left: 522px; top: 152px; color: var(--text); }
  .person-name { font-weight: 600; font-size: 27px; line-height: 34px; }
  .person-title { font-size: 27px; line-height: 34px; }
  .contact-list { position: absolute; left: 522px; top: 235px; list-style: none; color: var(--text); }
  .contact-item { display: flex; align-items: center; gap: 9px; height: 40px; font-size: 25px; }
  .contact-icon { width: 25px; height: 25px; flex: none; border-radius: 3px; background: linear-gradient(135deg, var(--aqua), var(--deep-blue)); display: flex; align-items: center; justify-content: center; }
  .contact-icon svg { width: 17px; height: 17px; }
</style>
</head>
<body>
  <section class="card card--front">
    <svg class="card-waves" viewBox="0 0 1063 638" preserveAspectRatio="none" aria-hidden="true">
      <defs>
        <linearGradient id="waveTop" x1="0" x2="1"><stop offset="0" stop-color="#1a6ee8"/><stop offset="1" stop-color="#33e8ee"/></linearGradient>
        <linearGradient id="waveBottom" x1="0" x2="1"><stop offset="0" stop-color="#33e8ee"/><stop offset="1" stop-color="#1a6ee8"/></linearGradient>
      </defs>
      <path fill="url(#waveTop)" d="M0 0 H1063 V77 C980 50 900 25 780 27 C600 30 400 100 180 101 C100 101 40 92 0 79 Z"/>
      <path fill="url(#waveBottom)" d="M0 562 C80 590 200 612 310 612 C520 612 760 538 930 538 C990 538 1030 550 1063 561 V638 H0 Z"/>
    </svg>
    <div class="brand">
      <span class="brand-mark"></span>
      <span class="brand-name">VEROSTEL</span>
    </div>
    <div class="person">
      <p class="person-name">Your Name</p>
      <p class="person-title">Manager</p>
    </div>
    <ul class="contact-list">
      <li class="contact-item">
        <span class="contact-icon"><svg viewBox="0 0 24 24" fill="#fff"><path d="M6.6 10.8a15 15 0 0 0 6.6 6.6l2.2-2.2a1 1 0 0 1 1-.25 11.4 11.4 0 0 0 3.6.57 1 1 0 0 1 1 1V20a1 1 0 0 1-1 1A17 17 0 0 1 3 4a1 1 0 0 1 1-1h3.5a1 1 0 0 1 1 1c0 1.25.2 2.45.57 3.57a1 1 0 0 1-.25 1z"/></svg></span>
        <span>123 444 555</span>
      </li>
      <li class="contact-item">
        <span class="contact-icon"><svg viewBox="0 0 24 24" fill="none" stroke="#fff" stroke-width="2"><path d="M12 21s-6-6.5-6-11a6 6 0 0 1 12 0c0 4.5-6 11-6 11z"/><circle cx="12" cy="10" r="2"/></svg></span>
        <span>789 Your Street Here</span>
      </li>
      <li class="contact-item">
        <span class="contact-icon"><svg viewBox="0 0 24 24" fill="none" stroke="#fff" stroke-width="2"><rect x="3" y="5" width="18" height="14"/><path d="M3 5l9 8 9-8M3 19l7-7M21 19l-7-7"/></svg></span>
        <span>info@yourname.com</span>
      </li>
      <li class="contact-item">
        <span class="contact-icon"><svg viewBox="0 0 24 24" fill="none" stroke="#fff" stroke-width="1.8"><circle cx="12" cy="12" r="9"/><ellipse cx="12" cy="12" rx="4" ry="9"/><path d="M3 12h18M5 7h14M5 17h14"/></svg></span>
        <span>www.yourname.com</span>
      </li>
    </ul>
  </section>

  <section class="card card--back">
    <svg class="card-waves" viewBox="0 0 1063 637" preserveAspectRatio="none" aria-hidden="true">
      <defs>
        <linearGradient id="waveBand" x1="0" x2="1"><stop offset="0" stop-color="#33e8ee"/><stop offset="1" stop-color="#1a6ee8"/></linearGradient>
      </defs>
      <path fill="url(#waveBand)" d="M0 75 C90 45 200 25 310 25 C520 25 760 101 960 101 C1000 101 1035 90 1063 76 V561 C1000 580 900 611 760 611 C560 611 360 537 200 537 C120 537 50 547 0 561 Z"/>
    </svg>
    <div class="brand">
      <span class="brand-mark"></span>
      <span class="brand-name">VEROSTEL</span>
    </div>
  </section>
</body>
</html>
```